Business card and company stationary - Corvane Cleaning Ltd

1. Who are we and who are our customers?

o We are a relatively new cleaning company, established December 2008. We are a small company. We have 24 staff and we offer domestic and commercial cleaning services.
o We both (me and my wife) have been working for many years in the cleaning industry. We worked for some of the biggest and best cleaning companies in UK. We’ve been operatives, supervisors and managers.
o Inevitably after so many years of working for someone else, we decided to start our own business.
o Our domestic customers are middle class families and busy professionals. We’ve got some commercial customers, mainly offices.
o We are growing steadily.

2. What do we do? What are our services?

o Cleaning. We’ve got range of services - not to many but still can be daunting and confusing for some.
o Generally we’ve got domestic and commercial clients. The approach to the domestic cleaning customers is different to the commercial. In the way we want to say that it is cleaning that we do, but we acknowledge the environment and we appreciate the personal circumstances and requirements that are present. We do care, we listen and we try to work out the best possible way to complete our work.
o Mainly we get our work through referrals

3. What do we want with our stationery ?

o To place and maintain our message and reach out to people and organisations
o We want to advertise, communicate and sale.
o We are going to sell services.
o Increase membership, loyalty and support.

We are after business card design, headed letter and compliment slip.
We would like the headed letter to be created in formats suitable for :
- printing format
- also for use in our daily correspondence via e mail with clients and staff in a easy to edit and write format

The website we have is still under contraction and the domain is corvanecleaning.example

Target Market(s)

Families, individuals, businesses.

Industry/Entity Type

Cleaning Service

Contact Information for Business Card

FRONT :
Company Name - Corvane Cleaning Ltd
Company address - 41 Pelbury Rd, Pelbury, Essex, RM14 7QT
Name - Mrs. Teodora Vasilkova - Tedi
Title - Managing Director
Company phone - 020 8837 2591
E mail - tedi.vasilkova@corvanecleaning.example

BACK :

Company website - corvanecleaning.example
E mail - enquiries@corvanecleaning.example

Font styles to use
Serif

Requirements
Must have
• The above items and company logo...maybe at the back. But I'm free for any suggestions.

```html
<!DOCTYPE html>
<html lang="en">
<head>
<meta charset="utf-8">
<title>Corvane Cleaning Ltd – Stationery</title>
<link rel="stylesheet" href="https://fonts.googleapis.com/css2?family=Lora:wght@400;500;600;700&display=swap">
<style>
  :root {
    --backdrop: #d1d2d4;
    --paper: #ffffff;
    --brand-blue: #35c5ef;
    --ink: #1c1c1c;
    --text: #3a3a3a;
    --faint: #ececec;
    --shadow: rgba(0,0,0,0.35);
  }
  * { margin: 0; padding: 0; box-sizing: border-box; }
  html, body { width: 1200px; height: 919px; overflow: hidden; }
  body {
    background: var(--backdrop);
    font-family: "Lora", serif;
    color: var(--text);
    position: relative;
  }
  .sheet {
    position: absolute;
    background: var(--paper);
    overflow: hidden;
    box-shadow: 4px 5px 7px var(--shadow);
  }
  .business-card { left: 85px; top: 88px; width: 361px; height: 216px; }
  .compliment-slip { left: 85px; top: 377px; width: 361px; height: 216px; }
  .letterhead { left: 545px; top: 83px; width: 582px; height: 763px; }

  /* brand lockup: plain circle + name */
  .brand { position: absolute; display: flex; flex-direction: column; align-items: center; }
  .brand-mark { border-radius: 50%; background: var(--brand-blue); }
  .brand-name {
    font-weight: 700; color: var(--ink); text-align: center;
    letter-spacing: 0.1em; line-height: 1.2; text-transform: uppercase;
  }
  .business-card .brand { left: 8px; top: 12px; width: 116px; }
  .business-card .brand-mark { width: 74px; height: 74px; }
  .business-card .brand-name { font-size: 11px; margin-top: 8px; }

  .letterhead .brand { left: 16px; top: 20px; width: 124px; }
  .letterhead .brand-mark { width: 78px; height: 78px; }
  .letterhead .brand-name { font-size: 12px; margin-top: 8px; }

  .compliment-slip .brand { right: 36px; top: 104px; }
  .compliment-slip .brand-mark { width: 86px; height: 86px; }

  /* faint background seal */
  .seal { position: absolute; border-radius: 50%; border: 5px solid var(--faint); }
  .compliment-slip .seal { left: -80px; top: 60px; width: 220px; height: 220px; border-width: 4px; }
  .letterhead .seal { left: -26px; top: 490px; width: 300px; height: 300px; border-width: 6px; }

  /* contact blocks */
  .contact { position: absolute; text-align: right; }
  .person-name { color: var(--brand-blue); font-weight: 500; font-size: 15.5px; letter-spacing: 0.04em; text-transform: uppercase; }
  .person-title { font-size: 8px; letter-spacing: 0.06em; text-transform: uppercase; margin-top: 1px; }
  .business-card .name-block { position: absolute; right: 13px; top: 11px; text-align: right; }
  .business-card .address { right: 13px; top: 80px; font-size: 8.5px; line-height: 1.35; text-transform: uppercase; }
  .business-card .details { right: 13px; top: 126px; font-size: 8.5px; line-height: 1.35; }
  .letterhead .address { right: 26px; top: 28px; font-size: 14px; line-height: 1.3; text-transform: uppercase; }
  .letterhead .details { right: 26px; top: 70px; font-size: 14px; line-height: 1.3; }

  .line { display: flex; justify-content: flex-end; align-items: center; gap: 5px; white-space: nowrap; }
  .icon { flex: none; fill: none; stroke: var(--brand-blue); stroke-width: 1.6; }
  .business-card .icon { width: 7px; height: 7px; }
  .letterhead .icon { width: 10px; height: 10px; }

  .slip-web { position: absolute; right: 16px; top: 194px; font-size: 8.5px; color: var(--ink); }
  .slip-web b { color: var(--brand-blue); font-weight: 600; }

  .swoosh { position: absolute; left: 0; bottom: 0; width: 100%; }
  .business-card .swoosh { height: 40px; }
  .letterhead .swoosh { height: 66px; }
</style>
</head>
<body>

<section class="sheet business-card" aria-label="Business card">
  <div class="brand">
    <div class="brand-mark"></div>
    <div class="brand-name">Corvane<br>Cleaning Ltd</div>
  </div>
  <div class="name-block">
    <div class="person-name">Teodora Vasilkova</div>
    <div class="person-title">Managing Director</div>
  </div>
  <div class="contact address">41 Pelbury Rd<br>Pelbury, Essex RM14 7QT</div>
  <div class="contact details">
    <div class="line">020 8837 2591 <svg class="icon" viewBox="0 0 10 10"><rect x="2.5" y="0.8" width="5" height="8.4" rx="1"/></svg></div>
    <div class="line">020 8837 2590 <svg class="icon" viewBox="0 0 10 10"><path d="M2 1l2 2-1 1.5c.8 1.3 1.7 2.2 3 3L7.5 6l2 2-1.5 1.5C4.5 9 1 5.5.5 2z"/></svg></div>
    <div class="line">tedi.vasilkova@corvanecleaning.example <svg class="icon" viewBox="0 0 10 10"><rect x="1" y="2.5" width="8" height="5.5"/><path d="M1 2.5l4 3 4-3"/></svg></div>
    <div class="line">www.corvanecleaning.example <svg class="icon" viewBox="0 0 10 10"><circle cx="5" cy="5" r="4"/><path d="M1 5h8M5 1c-2 2.5-2 5.5 0 8M5 1c2 2.5 2 5.5 0 8"/></svg></div>
  </div>
  <svg class="swoosh" viewBox="0 0 400 40" preserveAspectRatio="none" aria-hidden="true">
    <path d="M0 12 Q200 36 400 10 L400 40 L0 40 Z" fill="var(--brand-blue)"/>
    <path d="M0 3 Q200 28 400 2" fill="none" stroke="var(--ink)" stroke-width="2"/>
  </svg>
</section>

<section class="sheet compliment-slip" aria-label="Compliment slip">
  <div class="seal" aria-hidden="true"></div>
  <div class="brand"><div class="brand-mark"></div></div>
  <div class="slip-web">www.<b>corvanecleaning</b>.example</div>
</section>

<section class="sheet letterhead" aria-label="Headed letter">
  <div class="seal" aria-hidden="true"></div>
  <div class="brand">
    <div class="brand-mark"></div>
    <div class="brand-name">Corvane<br>Cleaning Ltd</div>
  </div>
  <div class="contact address">41 Pelbury Rd<br>Pelbury, Essex RM14 7QT</div>
  <div class="contact details">
    <div class="line">020 8837 2591 <svg class="icon" viewBox="0 0 10 10"><rect x="2.5" y="0.8" width="5" height="8.4" rx="1"/></svg></div>
    <div class="line">020 8837 2590 <svg class="icon" viewBox="0 0 10 10"><path d="M2 1l2 2-1 1.5c.8 1.3 1.7 2.2 3 3L7.5 6l2 2-1.5 1.5C4.5 9 1 5.5.5 2z"/></svg></div>
    <div class="line">enquiries@corvanecleaning.example <svg class="icon" viewBox="0 0 10 10"><rect x="1" y="2.5" width="8" height="5.5"/><path d="M1 2.5l4 3 4-3"/></svg></div>
    <div class="line">www.corvanecleaning.example <svg class="icon" viewBox="0 0 10 10"><circle cx="5" cy="5" r="4"/><path d="M1 5h8M5 1c-2 2.5-2 5.5 0 8M5 1c2 2.5 2 5.5 0 8"/></svg></div>
  </div>
  <svg class="swoosh" viewBox="0 0 600 66" preserveAspectRatio="none" aria-hidden="true">
    <path d="M0 12 Q300 42 600 10 L600 66 L0 66 Z" fill="var(--brand-blue)"/>
    <path d="M0 2 Q300 36 600 1" fill="none" stroke="var(--ink)" stroke-width="2.2"/>
  </svg>
</section>

</body>
</html>
```